Vina Solvara

Solvara embodies the purity and intensity of Chile’s cold coastal terroir. The sleek white label and bold X logo reflect the stark beauty and unrelenting nature of these extreme winemaking conditions. Crisp, vibrant, and refreshingly bold, Solvara is a tribute to the wild energy of the Pacific winds and the cool embrace of the coastal valleys—a wine for those who seek purity and perfection in every sip. We would like to have a simple design focusing o the X, we try some option see attach but we are no satisfied is not enaguh eyes catching
Updates

Please create a mysterious, enigmatic label based on the typography and logo attached to the project. We need at least, at the entry level, five varietal products such as Carménère, Cabernet Sauvignon, Merlot, Chardonnay, and Malbec. Later, we would like to add more premium products, like a Reserva, a Special Reserva, or a Limited Edition. The design should be flexible and easily adaptable to accommodate various products while maintaining the same overall aesthetic.

I upload some wines label with printing technic we would like to use on our label, please incorporate this into your design

Project Brief – Large-Scale Brand Label Design
We are developing a new large-scale brand with a structured range of wines. Below are the key design elements and specifications for the labels:

Pinot Noir, Chardonnay, Syrah (Burgundy bottle shape – must include "Special Reserve" on the label)
General Label Guidelines
Year: Only mention "2024" (do not include the word “vintage”).
Capsules: Use standard-colored capsules only (no branding).
Label Design:
Focus on the label itself; bottle and background are irrelevant.
We can consider a wraparound label, but space must be reserved for back-label information.
Please refer to www.pelnorth-wines.example for brand coherence. Let us know if further details are needed.

Target Market(s)

peopels who looking for simple design but strinking with the X . THe X could be like a painting brush somehting which make it look artistic

Industry/Entity Type

Wines producer

Font styles to use
Decorative
Script
Other font styles liked:
• the X would be nice if it look like he is Brush from a painter

Colors
0054AA
0677BA
7BADD7
CADEEF
E8F1F8
FFF300
FFF600
FEFA6F
FFFEC7
FFFEE8
EB3D1F
EC4F4E
F09395
F8D3D4
FCEDEE

Requirements
Must have
• We need to indicate the varietals Cabernet Sauvignon, the vintage 2024, the region DO Central Valley
Nice to have
• option on a burgendy bottle for chardonnay and pinot noir and option on bordeau bottle for Cabernet sauvignon and Merlot, We will need a large serie of 5 entrance lebvel (4 red one white) 2 reserve, 2 special reserve, 2 Limited

```html
<!DOCTYPE html>
<html lang="en">
<head>
<meta charset="utf-8">
<title>Special Reserve 2024 – Label Series</title>
<link href="https://fonts.googleapis.com/css2?family=Bodoni+Moda:opsz,wght@6..96,400;6..96,500&display=swap" rel="stylesheet">
<style>
  :root {
    --backdrop: #a9a9a9;
    --pinot-x: #0c1c66;
    --pinot-paint-light: #3f7f98;
    --pinot-paint-mid: #1f4f78;
    --pinot-paint-dark: #0f2454;
    --chard-x: #f8f3d2;
    --chard-paint-light: #ecd9b3;
    --chard-paint-mid: #e9b95a;
    --chard-paint-dark: #dc9a22;
    --syrah-x: #780808;
    --syrah-paint-light: #f0331f;
    --syrah-paint-mid: #d41612;
    --syrah-paint-dark: #8c0c0c;
    --ink-light: #ffffff;
    --ink-dark: #3b2a18;
  }
  * { margin: 0; padding: 0; box-sizing: border-box; }
  html, body {
    width: 1200px; height: 960px; overflow: hidden;
    background: var(--backdrop);
    font-family: "Bodoni Moda", "Times New Roman", serif;
  }
  .label-series {
    position: absolute; inset: 0;
    display: flex; justify-content: center; align-items: center;
    gap: 40px;
  }
  .label {
    position: relative;
    width: 340px; height: 340px;
    color: var(--ink-light);
    box-shadow: 0 6px 18px rgba(0,0,0,0.18);
    overflow: hidden;
  }
  .label--chardonnay { color: var(--ink-dark); }
  .label__art { position: absolute; inset: 0; width: 100%; height: 100%; display: block; }
  .label__text { position: absolute; text-align: center; line-height: 1.2; font-weight: 400; }
  .label__region { top: 7.5%; left: 0; right: 0; font-size: 12px; }
  .label__tier { top: 50%; left: 7%; transform: translateY(-50%); font-size: 13px; }
  .label__year { top: 50%; right: 12%; transform: translateY(-50%); font-size: 13px; }
  .label__varietal {
    top: 50%; left: 0; right: 0; transform: translateY(-50%);
    font-size: 29px; font-weight: 500; line-height: 1.02; letter-spacing: 0.02em;
  }
  .label__style { bottom: 7%; left: 0; right: 0; font-size: 12px; }
</style>
</head>
<body>
<main class="label-series">

  <section class="label label--pinot">
    <svg class="label__art" viewBox="0 0 100 100" preserveAspectRatio="none" role="img" aria-label="Blue and teal painted brushstrokes around a bold deep-blue X">
      <defs>
        <linearGradient id="pinot-paint" x1="0" y1="0" x2="1" y2="1">
          <stop offset="0" stop-color="var(--pinot-paint-light)"/>
          <stop offset="0.45" stop-color="var(--pinot-paint-mid)"/>
          <stop offset="1" stop-color="var(--pinot-paint-dark)"/>
        </linearGradient>
      </defs>
      <rect width="100" height="100" fill="var(--pinot-x)"/>
      <g fill="url(#pinot-paint)">
        <polygon points="18,0 88,0 52,34"/>
        <polygon points="12,100 90,100 51,67"/>
        <polygon points="0,16 0,86 33,51"/>
        <polygon points="100,12 100,90 68,51"/>
      </g>
    </svg>
    <p class="label__text label__region">DO<br>Central Valley</p>
    <p class="label__text label__tier">Special<br>Reserve</p>
    <h2 class="label__text label__varietal">Pinot<br>noir</h2>
    <p class="label__text label__year">20<br>24</p>
    <p class="label__text label__style">Red Wine</p>
  </section>

  <section class="label label--chardonnay">
    <svg class="label__art" viewBox="0 0 100 100" preserveAspectRatio="none" role="img" aria-label="Ochre and sand painted brushstrokes around a bold cream X">
      <defs>
        <linearGradient id="chard-paint" x1="0" y1="1" x2="1" y2="0">
          <stop offset="0" stop-color="var(--chard-paint-dark)"/>
          <stop offset="0.5" stop-color="var(--chard-paint-mid)"/>
          <stop offset="1" stop-color="var(--chard-paint-light)"/>
        </linearGradient>
      </defs>
      <rect width="100" height="100" fill="var(--chard-x)"/>
      <g fill="url(#chard-paint)">
        <polygon points="18,0 88,0 52,34"/>
        <polygon points="12,100 90,100 51,67"/>
        <polygon points="0,16 0,86 33,51"/>
        <polygon points="100,12 100,90 68,51"/>
      </g>
    </svg>
    <p class="label__text label__region">DO<br>Central Valley</p>
    <p class="label__text label__tier">Special<br>Reserve</p>
    <h2 class="label__text label__varietal">Char<br>donnay</h2>
    <p class="label__text label__year">20<br>24</p>
    <p class="label__text label__style">White Wine</p>
  </section>

  <section class="label label--syrah">
    <svg class="label__art" viewBox="0 0 100 100" preserveAspectRatio="none" role="img" aria-label="Bright red painted brushstrokes around a bold dark-red X">
      <defs>
        <linearGradient id="syrah-paint" x1="0" y1="0" x2="1" y2="1">
          <stop offset="0" stop-color="var(--syrah-paint-light)"/>
          <stop offset="0.5" stop-color="var(--syrah-paint-mid)"/>
          <stop offset="1" stop-color="var(--syrah-paint-dark)"/>
        </linearGradient>
      </defs>
      <rect width="100" height="100" fill="var(--syrah-x)"/>
      <g fill="url(#syrah-paint)">
        <polygon points="18,0 88,0 52,34"/>
        <polygon points="12,100 90,100 51,67"/>
        <polygon points="0,16 0,86 33,51"/>
        <polygon points="100,12 100,90 68,51"/>
      </g>
    </svg>
    <p class="label__text label__region">DO<br>Central Valley</p>
    <p class="label__text label__tier">Special<br>Reserve</p>
    <h2 class="label__text label__varietal">Syrah</h2>
    <p class="label__text label__year">20<br>24</p>
    <p class="label__text label__style">Red Wine</p>
  </section>

</main>
</body>
</html>
```